Project Meridel PowerPoint Design

This is a PPT design for Power & Utilities company who are in the process of a technology upgrade for their Finance department. We are looking to develop a branded PPT for Project Meridel (specifically MERIDEL). Why does Meridel resonate? "The Earth is pointed almost directly at Meridel. During the course of the night,
Meridel does not rise or set, but remains in nearly the same spot above the
northern horizon year- round while the other stars circle around it."
Meridel represents the guiding principles that manage, monitor and
control the organizations financials.

Target Market(s)

Finance stakeholders impacted by technology enhancement

Font styles to use
Serif
Other font styles liked:
• Arial

Colors
0054AA
0677BA
7BADD7
CADEEF
E8F1F8

Requirements
Must have
• Various slide layout ( Cover slide, content slide, divider, etc). Attached is the logo and corporate colors
Nice to have
• Over the top creativity

```html
<!DOCTYPE html>
<html lang="en">
<head>
<meta charset="utf-8">
<title>Project Meridel – Presentation Template</title>
<link href="https://fonts.googleapis.com/css2?family=Roboto:wght@400;500;700&display=swap" rel="stylesheet">
<style>
:root{
  --board:#1a1b1d;
  --blue:#2d5fc0;
  --blue-deep:#0054aa;
  --blue-mid:#0677ba;
  --blue-soft:#7badd7;
  --ink:#222;
  --grey:#8e9096;
  --grey-light:#c9cacd;
  --white:#fff;
  --red:#f21a1a;
  --navy:#0f1670;
  --amber:#f7b500;
  --maroon:#8c1040;
  --orange:#f58a0a;
  --gold:#b8860b;
  --rust:#c04a1b;
  --wine:#8b1a2b;
}
*{margin:0;padding:0;box-sizing:border-box}
html,body{width:667px;height:1200px;overflow:hidden;background:var(--board);font-family:"Roboto",Arial,sans-serif;color:var(--ink)}
.board{position:relative;width:667px;height:1200px}
.slide{position:absolute;overflow:hidden;background:var(--white)}
.abs{position:absolute}
.photo{position:absolute}

/* brand name */
.brand{position:absolute;color:var(--blue);font-weight:500;line-height:1;white-space:nowrap}
.brand span{display:block}

/* footer */
.footer{position:absolute;left:0;right:0;bottom:0;height:19px}
.footer .tab{position:absolute;left:0;bottom:0;width:64px;height:19px;background:#8a8c92;clip-path:polygon(0 0,86% 0,100% 100%,0 100%)}
.footer .tab .brand{left:12px;top:4px;font-size:4.6px;letter-spacing:.6px}
.footer .tab .brand span+span{font-size:7px;letter-spacing:.4px}
.footer .rule{position:absolute;left:64px;right:18px;top:8px;height:1.2px;background:#9a9ca1}
.footer .url{position:absolute;left:67px;top:11px;font-size:3.8px;color:#777;letter-spacing:.1px}
.footer .page{position:absolute;right:10px;top:2px;width:13px;height:13px;border-radius:50%;background:var(--blue-deep);border:2px solid #d7dbe3;color:#fff;font-size:4.4px;display:flex;align-items:center;justify-content:center;font-weight:500}

/* headers */
.head{position:absolute;left:10px;border-left:1px solid var(--blue-deep);padding-left:3px}
.head h2{font-weight:400;color:var(--blue-deep);font-size:7px;line-height:1.2}
.head p{font-size:3.8px;color:#444;margin-top:2px}

/* section dividers */
.num{position:absolute;width:19px;height:19px;border-radius:50%;border:1px solid currentColor;display:flex;align-items:center;justify-content:center;font-size:8px;font-weight:500}
.sec-title{position:absolute;font-size:9px;font-weight:400;letter-spacing:.2px}
.sec-body{position:absolute;font-size:4px;line-height:1.3}

.lorem{position:absolute;font-size:4.1px;line-height:1.22;text-align:justify;color:#333}
.centered{text-align:center}
.year{font-size:7px;fill:#fff;font-family:"Roboto",Arial,sans-serif}
.tl-note{position:absolute;font-size:3.8px;line-height:1.25;text-align:right;color:#333;width:40px}
</style>
</head>
<body>
<div class="board">

  <!-- 1 Cover -->
  <section class="slide" style="left:20px;top:38px;width:301px;height:209px">
    <div class="photo" role="img" aria-label="Starfield over a glowing blue digital horizon grid" style="inset:0;background:radial-gradient(ellipse 70% 40% at 55% 100%,#1f8cff 0%,#0a3f9a 35%,rgba(3,10,30,0) 75%),linear-gradient(#03060f,#061024 70%,#0b2a66)"></div>
    <div class="brand" style="left:38px;top:64px;font-size:19px;letter-spacing:4px">
      <span style="padding-left:100px;font-size:17px">PROJECT</span>
      <span style="font-size:36px;letter-spacing:3px;margin-top:4px">MERIDEL</span>
    </div>
  </section>

  <!-- 2 Introduction -->
  <section class="slide" style="left:341px;top:38px;width:300px;height:210px">
    <div class="photo" role="img" aria-label="Hands sketching financial notes beside a laptop" style="left:0;top:0;width:300px;height:135px;background:linear-gradient(120deg,#6c7f86,#9fb3b5 45%,#5e4a3c 80%,#8a9ea2)"></div>
    <svg class="abs" style="left:0;top:0" width="300" height="210" viewBox="0 0 300 210">
      <path d="M0 118 Q140 62 300 134 L300 210 L0 210Z" fill="#fff"/>
      <path d="M0 116 Q140 58 300 130" fill="none" stroke="var(--blue)" stroke-width="3"/>
    </svg>
    <h1 class="abs" style="left:0;right:0;top:118px;text-align:center;font-size:9px;font-weight:700;color:#222">INTRODUCTION</h1>
    <p class="lorem" style="left:16px;width:265px;top:132px;text-align:left">Lorem ipsum dolor sit amet, consectetur adipiscing elit, sed do eiusmod tempor incididunt ut labore et dolore magna aliqua. Quis ipsum suspendisse ultrices gravida. Risus commodo viverra maecenas accumsan lacus vel facilisis.</p>
    <p class="lorem" style="left:16px;width:265px;top:157px;text-align:left">Lorem ipsum dolor sit amet, consectetur adipiscing elit, sed do eiusmod tempor incididunt ut labore et dolore magna aliqua. Quis ipsum suspendisse ultrices gravida. Risus commodo viverra maecenas accumsan lacus vel facilisis.</p>
    <div class="footer"><div class="tab"><div class="brand"><span>PROJECT</span><span>MERIDEL</span></div></div><div class="rule"></div><div class="url">WWW.PROJECTMERIDEL.COM</div><div class="page">1</div></div>
  </section>

  <!-- 3 Section 01 -->
  <section class="slide" style="left:20px;top:269px;width:301px;height:210px;color:#fff">
    <div class="photo" role="img" aria-label="Night sky above the curve of the Earth" style="inset:0;background:radial-gradient(ellipse 80% 22% at 50% 100%,#2a3f55 0%,#0d141d 60%,#000 100%),#000"></div>
    <div class="num" style="left:26px;top:82px">01</div>
    <div class="sec-title" style="left:51px;top:86px">SECTION TITLE</div>
    <p class="sec-body" style="left:52px;top:100px;width:130px">Lorem Ipsum is simply dummy text of the printing and typesetting industry.Lorem Ipsum is simply dummy text of the printing and typesetting industry.</p>
    <div class="brand" style="left:198px;top:91px;letter-spacing:1.5px"><span style="font-size:6px;padding-left:30px">PROJECT</span><span style="font-size:15px;margin-top:1px">MERIDEL</span></div>
  </section>

  <!-- 4 Our services -->
  <section class="slide" style="left:341px;top:269px;width:300px;height:210px">
    <div class="photo" role="img" aria-label="Hand reaching into glowing stock market charts" style="left:0;top:0;width:300px;height:130px;background:linear-gradient(90deg,#2f5b6e,#8a5b3e 40%,#1f6b7c 65%,#0e3a52)"></div>
    <div class="abs" style="left:11px;top:7px;border-left:1px solid #fff;padding-left:3px;color:#fff;font-size:7px;line-height:11px">OUR SERVICES</div>
    <svg class="abs" style="left:0;top:0" width="300" height="210" viewBox="0 0 300 210">
      <path d="M0 124 Q150 52 300 124 L300 210 L0 210Z" fill="#fff"/>
      <path d="M0 121 Q150 49 300 121" fill="none" stroke="var(--blue)" stroke-width="3"/>
      <g fill="#fff">
        <circle cx="38" cy="106" r="15"/><circle cx="114" cy="90" r="15"/><circle cx="180" cy="90" r="15"/><circle cx="261" cy="110" r="15"/>
      </g>
      <g fill="none" stroke-width=".8" stroke-linecap="round">
        <g stroke="var(--gold)"><path d="M31 113h14M33 113v-4M37 113v-6M41 113v-8M31 106l5-4 3 2 5-5"/></g>
        <g stroke="var(--rust)"><rect x="108" y="83" width="12" height="9" rx="1"/><path d="M112 95h4M114 92v3"/><circle cx="114" cy="87" r="2"/></g>
        <g stroke="var(--wine)"><circle cx="180" cy="85" r="3"/><path d="M174 96q6-8 12 0z"/></g>
        <g stroke="var(--red)"><circle cx="261" cy="104" r="3"/><circle cx="256" cy="114" r="2"/><circle cx="261" cy="114" r="2"/><circle cx="266" cy="114" r="2"/></g>
      </g>
    </svg>
    <h3 class="abs centered" style="left:8px;width:60px;top:125px;font-size:5px;color:var(--gold)">HEADING1</h3>
    <p class="abs centered" style="left:8px;width:60px;top:135px;font-size:4.3px;line-height:1.45;color:#333">Lorem ipsum dolor sit amet, consectetur adipiscing elit, sed do eiusmod tempor incididunt ut labore et dolore magna aliqua. Quis ipsum</p>
    <h3 class="abs centered" style="left:82px;width:64px;top:121px;font-size:5px;color:var(--rust)">HEADING2</h3>
    <p class="abs centered" style="left:82px;width:64px;top:131px;font-size:4.3px;line-height:1.45;color:#333">Lorem ipsum dolor sit amet, consectetur adipiscing elit, sed do eiusmod tempor incididunt ut labore et dolore magna aliqua. Quis ipsum suspendisse ultrices gravida. Risus</p>
    <h3 class="abs centered" style="left:150px;width:64px;top:121px;font-size:5px;color:var(--wine)">HEADING3</h3>
    <p class="abs centered" style="left:150px;width:64px;top:131px;font-size:4.3px;line-height:1.45;color:#333">Lorem ipsum dolor sit amet, consectetur adipiscing elit, sed do eiusmod tempor incididunt ut labore et dolore magna aliqua. Quis ipsum suspendisse ultrices</p>
    <h3 class="abs centered" style="left:230px;width:62px;top:130px;font-size:5px;color:#a01c28">HEADING4</h3>
    <p class="abs centered" style="left:230px;width:62px;top:142px;font-size:4.3px;line-height:1.45;color:#333">Lorem ipsum dolor sit amet, consectetur adipiscing elit, sed do eiusmod tempor incididunt ut labore et dolore magna</p>
    <div class="footer"><div class="tab"><div class="brand"><span>PROJECT</span><span>MERIDEL</span></div></div><div class="rule"></div><div class="url">WWW.PROJECTMERIDEL.COM</div><div class="page">2</div></div>
  </section>

  <!-- 5 Image at left -->
  <section class="slide" style="left:21px;top:497px;width:300px;height:204px">
    <div class="head" style="top:19px"><h2>Image at left with the text</h2><p>subtitle goes here</p></div>
    <div class="abs" style="left:0;top:52px;width:22px;height:113px;border-top:2px solid var(--blue-soft);border-bottom:2px solid var(--blue-soft)"></div>
    <div class="abs" style="left:115px;top:52px;width:33px;height:113px;border:2px solid var(--grey);border-left:0"></div>
    <div class="photo" role="img" aria-label="Businessman holding a tablet with a glowing bar chart" style="left:1px;top:55px;width:144px;height:107px;background:radial-gradient(ellipse 40% 40% at 55% 55%,#2ad1c0,#1e5c5a 60%,#1d3a3c)"></div>
    <h3 class="abs" style="left:162px;top:59px;font-size:7px;font-weight:400;color:var(--blue-deep)">Subtitle here</h3>
    <p class="lorem" style="left:162px;top:77px;width:111px">Lorem ipsum dolor sit amet, consectetur adipiscing elit, sed do eiusmod tempor incididunt ut labore et dolore magna aliqua. Quis ipsum suspendisse ultrices gravida. Risus commodo viverra maecenas accumsan lacus vel facilisis.<br>Lorem ipsum dolor sit amet, consectetur adipiscing elit, sed do eiusmod tempor incididunt ut labore et dolore magna aliqua. Quis ipsum suspendisse ultrices gravida. Risus commodo viverra maecenas accumsan lacus vel facilisis.<br>Lorem ipsum dolor sit amet, consectetur adipiscing elit, sed do eiusmod tempor incididunt ut labore et dolore magna aliqua. Quis ipsum suspendisse ultrices gravida. Risus commodo viverra maecenas accumsan lacus vel facilisis.</p>
    <div class="footer"><div class="tab"><div class="brand"><span>PROJECT</span><span>MERIDEL</span></div></div><div class="rule"></div><div class="url">WWW.PROJECTMERIDEL.COM</div><div class="page">3</div></div>
  </section>

  <!-- 6 Section 02 -->
  <section class="slide" style="left:341px;top:497px;width:300px;height:204px;color:#111">
    <div class="photo" role="img" aria-label="Looking up at pale glass skyscrapers" style="inset:0;background:linear-gradient(100deg,#d8d8d8 0%,#f7f7f7 35%,#ffffff 55%,#cfcfcf 85%,#b9b9b9)"></div>
    <div class="brand" style="left:48px;top:33px;letter-spacing:1.5px"><span style="font-size:6px;padding-left:30px">PROJECT</span><span style="font-size:15px;margin-top:1px">MERIDEL</span></div>
    <div class="num" style="left:22px;top:55px">02</div>
    <div class="sec-title" style="left:47px;top:59px">SECTION TITLE</div>
    <p class="sec-body" style="left:48px;top:72px;width:130px">Lorem Ipsum is simply dummy text of the printing and typesetting industry.Lorem Ipsum is simply dummy text of the printing and typesetting industry.</p>
  </section>

  <!-- 7 Timeline -->
  <section class="slide" style="left:21px;top:723px;width:300px;height:213px">
    <div class="head" style="top:20px"><h2 style="line-height:14px">Timeline Infographics</h2></div>
    <div class="tl-note" style="left:18px;top:63px">Lorem ipsum dolor sit amet, consectetur</div>
    <div class="tl-note" style="left:123px;top:63px">Lorem ipsum dolor sit amet, consectetur</div>
    <div class="tl-note" style="left:227px;top:63px">Lorem ipsum dolor sit amet, consectetur</div>
    <div class="tl-note" style="left:70px;top:132px">Lorem ipsum dolor sit amet, consectetur</div>
    <div class="tl-note" style="left:174px;top:132px">Lorem ipsum dolor sit amet, consectetur</div>
    <svg class="abs" style="left:0;top:0" width="300" height="213" viewBox="0 0 300 213">
      <g stroke-width="1">
        <line x1="60" y1="63" x2="60" y2="104" stroke="var(--red)"/>
        <line x1="164" y1="63" x2="164" y2="104" stroke="var(--amber)"/>
        <line x1="268" y1="63" x2="268" y2="104" stroke="var(--orange)"/>
        <line x1="112" y1="124" x2="112" y2="167" stroke="var(--navy)"/>
        <line x1="216" y1="124" x2="216" y2="167" stroke="var(--maroon)"/>
      </g>
      <g stroke="#fff" stroke-width="2.5">
        <path d="M230 103h34a11 11 0 0 1 0 22h-34z" fill="var(--orange)"/>
        <path d="M178 103h38a11 11 0 0 1 0 22h-38z" fill="var(--maroon)"/>
        <path d="M126 103h38a11 11 0 0 1 0 22h-38z" fill="var(--amber)"/>
        <path d="M73 103h39a11 11 0 0 1 0 22h-39z" fill="var(--navy)"/>
        <path d="M20 103h42a11 11 0 0 1 0 22h-42z" fill="var(--red)"/>
      </g>
      <text class="year" x="44" y="116.5" text-anchor="middle">YEAR1</text>
      <text class="year" x="100" y="116.5" text-anchor="middle">YEAR2</text>
      <text class="year" x="151" y="116.5" text-anchor="middle">YEAR3</text>
      <text class="year" x="201" y="116.5" text-anchor="middle">YEAR4</text>
      <text class="year" x="255" y="116.5" text-anchor="middle">YEAR5</text>
    </svg>
    <div class="footer"><div class="tab"><div class="brand"><span>PROJECT</span><span>MERIDEL</span></div></div><div class="rule"></div><div class="url">WWW.PROJECTMERIDEL.COM</div><div class="page">4</div></div>
  </section>

  <!-- 8 Section 03 -->
  <section class="slide" style="left:341px;top:723px;width:299px;height:213px;color:#fff">
    <div class="photo" role="img" aria-label="Dim business handshake" style="inset:0;background:radial-gradient(ellipse 50% 40% at 60% 45%,#3a3430,#1d1d1f 70%,#141416)"></div>
    <div class="brand" style="left:23px;top:29px;letter-spacing:1.5px"><span style="font-size:6px;padding-left:30px">PROJECT</span><span style="font-size:15px;margin-top:1px">MERIDEL</span></div>
    <div class="num" style="left:23px;top:78px">03</div>
    <div class="sec-title" style="left:48px;top:82px">SECTION TITLE</div>
    <p class="sec-body" style="left:49px;top:95px;width:130px">Lorem Ipsum is simply dummy text of the printing and typesetting industry.Lorem Ipsum is simply dummy text of the printing and typesetting industry.</p>
  </section>

  <!-- 9 Image at right -->
  <section class="slide" style="left:21px;top:953px;width:300px;height:213px">
    <div class="head" style="top:19px"><h2>Image at right with the text</h2><p>subtitle goes here</p></div>
    <h3 class="abs" style="left:9px;top:63px;font-size:7px;font-weight:400;color:var(--blue-deep)">Subtitle here</h3>
    <p class="lorem" style="left:9px;top:80px;width:111px">Lorem ipsum dolor sit amet, consectetur adipiscing elit, sed do eiusmod tempor incididunt ut labore et dolore magna aliqua. Quis ipsum suspendisse ultrices gravida. Risus commodo viverra maecenas accumsan lacus vel facilisis.<br>Lorem ipsum dolor sit amet, consectetur adipiscing elit, sed do eiusmod tempor incididunt ut labore et dolore magna aliqua. Quis ipsum suspendisse ultrices gravida. Risus commodo viverra maecenas accumsan lacus vel facilisis.<br>Lorem ipsum dolor sit amet, consectetur adipiscing elit, sed do eiusmod tempor incididunt ut labore et dolore magna aliqua. Quis ipsum suspendisse ultrices gravida. Risus commodo viverra maecenas accumsan lacus vel facilisis.</p>
    <div class="abs" style="left:142px;top:54px;width:30px;height:117px;border:2px solid var(--blue-soft);border-right:0"></div>
    <div class="abs" style="left:268px;top:54px;width:32px;height:117px;border-top:2px solid var(--grey);border-bottom:2px solid var(--grey)"></div>
    <div class="photo" role="img" aria-label="Team working on laptops around a wooden table" style="left:144px;top:57px;width:156px;height:111px;background:linear-gradient(160deg,#6a6766,#8a8582 40%,#a06a3e 70%,#4e3a2c)"></div>
    <div class="footer"><div class="tab"><div class="brand"><span>PROJECT</span><span>MERIDEL</span></div></div><div class="rule"></div><div class="url">WWW.PROJECTMERIDEL.COM</div><div class="page">5</div></div>
  </section>

  <!-- 10 Section 04 -->
  <section class="slide" style="left:342px;top:953px;width:298px;height:213px;color:#111">
    <div class="photo" role="img" aria-label="Laptop showing a finance dashboard on a desk" style="inset:0;background:linear-gradient(100deg,#2b2f3a 0%,#5d6270 35%,#b6b0aa 65%,#e4e1de 100%)"></div>
    <div class="brand" style="right:10px;top:26px;letter-spacing:1.5px;text-align:right"><span style="font-size:6px">PROJECT</span><span style="font-size:15px;margin-top:1px">MERIDEL</span></div>
    <div class="num" style="left:204px;top:52px">04</div>
    <div class="sec-title" style="left:226px;top:56px">SECTION TITLE</div>
    <p class="sec-body" style="right:10px;top:78px;width:92px;text-align:right">Lorem Ipsum is simply dummy text of the printing and typesetting industry.Lorem Ipsum is simply dummy text of the printing and</p>
  </section>

</div>
</body>
</html>
```